Valmora Holdings - Tidal Crest Car Wash automatic car wash signage

We are wanting to have a new automatic car wash sign designed. Our current one is dated and there are numerous options that are no longer available. We like the look of a clean sharp design in keeping with the Tidal Crest colours; orange and blues. The sign should have the Ultimate and Premium options, the "Tidal Crest" and Tidal Crest Car Wash designed in a clean, concise and cool manner.

Font styles to use
Sans Serif

Colors
f37122
3276b5
0255a3
34a7d8

Requirements
Must have
• This project must have the Ultimate and Premium options, the "bucket" and the Tidal Crest Car Wash title. The orange is a key colour with blues for water.

```html
<!DOCTYPE html>
<html lang="en">
<head>
<meta charset="utf-8">
<title>Tidal Crest Car Wash – Wash Menu Sign</title>
<link rel="stylesheet" href="https://fonts.googleapis.com/css2?family=Anton&family=Arimo:wght@700&display=swap">
<style>
  :root {
    --orange: #f37122;
    --orange-light: #f7941d;
    --red: #e8201f;
    --blue-deep: #0b3a84;
    --blue-mid: #0255a3;
    --blue-sky: #34a7d8;
    --row-blue: #bfe3f7;
    --black: #000000;
    --price-yellow: #fff200;
    --white: #ffffff;
    --stage: #6a6a6a;
  }
  * { margin: 0; padding: 0; box-sizing: border-box; }
  html, body { width: 1200px; height: 625px; overflow: hidden; background: var(--stage); }
  .sign {
    position: absolute; left: 20px; top: 40px; width: 1160px; height: 546px;
    background: var(--white); overflow: hidden;
  }
  .sign__backdrop {
    position: absolute; inset: 0;
    background: radial-gradient(ellipse at 50% 50%, #ffffff 45%, #e3f1fb 100%);
  }
  .sign__title {
    position: absolute; left: 40px; top: 52px;
    font-family: "Anton", "Impact", sans-serif; font-size: 84px; line-height: 1;
    letter-spacing: 1px; white-space: nowrap;
  }
  .sign__title-warm {
    background: linear-gradient(180deg, var(--red) 10%, var(--orange-light) 95%);
    -webkit-background-clip: text; background-clip: text; color: transparent;
  }
  .sign__title-cool {
    background: linear-gradient(180deg, var(--blue-deep) 10%, var(--blue-mid) 95%);
    -webkit-background-clip: text; background-clip: text; color: transparent;
  }
  .brand {
    position: absolute; left: 40px; top: 200px; width: 240px; height: 230px;
    display: flex; flex-direction: column; align-items: center; justify-content: center; gap: 14px;
  }
  .brand__dot { width: 96px; height: 96px; border-radius: 50%; background: var(--blue-sky); }
  .brand__name {
    font-family: "Arimo", "Arial", sans-serif; font-weight: 700; font-size: 40px; line-height: 1.05;
    color: var(--orange); text-align: center;
  }
  .features { position: absolute; left: 300px; top: 149px; width: 577px; list-style: none; }
  .features__row {
    height: 31px; margin-bottom: 6.1px; display: flex; align-items: center;
    background: linear-gradient(90deg, rgba(191,227,247,0) 0%, var(--row-blue) 12%, var(--row-blue) 100%);
    font-family: "Arimo", "Arial", sans-serif; font-weight: 700; font-size: 23.5px;
    color: var(--blue-deep); white-space: nowrap;
  }
  .features__star { color: var(--red); font-size: 13px; width: 41px; padding-left: 19px; }
  .plan { position: absolute; top: 64px; width: 119px; }
  .plan--ultimate { left: 886px; }
  .plan--premium { left: 1013px; }
  .plan__name {
    height: 26px; border-radius: 4px 4px 0 0;
    background: linear-gradient(180deg, var(--red), var(--orange-light));
    font-family: "Arimo", "Arial", sans-serif; font-weight: 700; font-size: 17px;
    color: var(--white); text-align: center; line-height: 27px;
    text-shadow: 0 0 2px #5a1a00;
  }
  .plan__price {
    height: 53px; background: var(--black); color: var(--price-yellow);
    font-family: "Arimo", "Arial", sans-serif; font-weight: 700;
    display: flex; align-items: flex-start; justify-content: center; padding-top: 4px;
  }
  .plan__currency { font-size: 18px; margin-top: 4px; }
  .plan__amount { font-size: 44px; line-height: 1; letter-spacing: -1px; margin-top: 2px; }
  .plan__cents { font-size: 18px; margin-top: 4px; margin-left: 2px; }
  .plan__cells { margin-top: 6px; list-style: none; }
  .plan__cell {
    height: 31px; margin-bottom: 6.1px; background: var(--orange);
    display: flex; align-items: center; justify-content: center;
  }
  .plan__tick { width: 26px; height: 20px; }
</style>
</head>
<body>
<main class="sign">
  <div class="sign__backdrop" role="img" aria-label="Soft pattern of soap bubbles across the sign background"></div>

  <h1 class="sign__title"><span class="sign__title-warm">TIDAL CREST</span> <span class="sign__title-cool">CAR WASH</span></h1>

  <div class="brand">
    <span class="brand__dot"></span>
    <span class="brand__name">Tidal Crest</span>
  </div>

  <ul class="features">
    <li class="features__row"><span class="features__star">★</span>WINDSHIELD &amp; FRONT END BUG WASH</li>
    <li class="features__row"><span class="features__star">★</span>UNDER CARRIAGE &amp; WHEEL BLASTER</li>
    <li class="features__row"><span class="features__star">★</span>EXTRA PASS OF HIGH PRESSURE WASH</li>
    <li class="features__row"><span class="features__star">★</span>TRY FOAM CONDIATIONER/CLEANER</li>
    <li class="features__row"><span class="features__star">★</span>SIDE KICK DRYERS</li>
    <li class="features__row"><span class="features__star">★</span>WAX/SURFACE PROTECTANT</li>
    <li class="features__row"><span class="features__star">★</span>ON BOARD OVERHEAD DRYER</li>
    <li class="features__row"><span class="features__star">★</span>TWO PASSES OF PRE-SOAK</li>
    <li class="features__row"><span class="features__star">★</span>HIGH PRESSURE WASH PASS</li>
    <li class="features__row"><span class="features__star">★</span>SPOT FREE RIMSE</li>
  </ul>

  <svg width="0" height="0" style="position:absolute">
    <defs>
      <symbol id="tick" viewBox="0 0 26 20">
        <path d="M2 11 L9 17 L24 3" fill="none" stroke="#ffffff" stroke-width="3.2" stroke-linecap="round" stroke-linejoin="round"/>
      </symbol>
    </defs>
  </svg>

  <section class="plan plan--ultimate">
    <div class="plan__name">ULTIMATE</div>
    <div class="plan__price"><span class="plan__currency">$</span><span class="plan__amount">14</span><span class="plan__cents">00</span></div>
    <ul class="plan__cells">
      <li class="plan__cell"><svg class="plan__tick"><use href="#tick"/></svg></li>
      <li class="plan__cell"><svg class="plan__tick"><use href="#tick"/></svg></li>
      <li class="plan__cell"><svg class="plan__tick"><use href="#tick"/></svg></li>
      <li class="plan__cell"><svg class="plan__tick"><use href="#tick"/></svg></li>
      <li class="plan__cell"><svg class="plan__tick"><use href="#tick"/></svg></li>
      <li class="plan__cell"><svg class="plan__tick"><use href="#tick"/></svg></li>
      <li class="plan__cell"><svg class="plan__tick"><use href="#tick"/></svg></li>
      <li class="plan__cell"><svg class="plan__tick"><use href="#tick"/></svg></li>
      <li class="plan__cell"><svg class="plan__tick"><use href="#tick"/></svg></li>
      <li class="plan__cell"><svg class="plan__tick"><use href="#tick"/></svg></li>
    </ul>
  </section>

  <section class="plan plan--premium">
    <div class="plan__name">PREMIUM</div>
    <div class="plan__price"><span class="plan__currency">$</span><span class="plan__amount">12</span><span class="plan__cents">00</span></div>
    <ul class="plan__cells">
      <li class="plan__cell"></li>
      <li class="plan__cell"><svg class="plan__tick"><use href="#tick"/></svg></li>
      <li class="plan__cell"></li>
      <li class="plan__cell"></li>
      <li class="plan__cell"><svg class="plan__tick"><use href="#tick"/></svg></li>
      <li class="plan__cell"></li>
      <li class="plan__cell"><svg class="plan__tick"><use href="#tick"/></svg></li>
      <li class="plan__cell"><svg class="plan__tick"><use href="#tick"/></svg></li>
      <li class="plan__cell"><svg class="plan__tick"><use href="#tick"/></svg></li>
      <li class="plan__cell"><svg class="plan__tick"><use href="#tick"/></svg></li>
    </ul>
  </section>
</main>
</body>
</html>
```